Wordpress Design for brand building and advertising company

I would like something with great looking colors to match a logo as well and, call to action buttons. Needs to be mobile ready. I also need to be able to upload site to web hosting provider. This website will be about helping small business build a brand. I would like something built that would show that we are serious about what we do and look to improve someone business with our services.

Target Market(s)

Small business looking to build a brand.

Industry/Entity Type

Digital Marketing

Logo Text

Plovenda

Font styles to use
Sans Serif

Colors

Designer to choose colors to be used in the design.

Requirements
Must have
• Call to action with contact form.
• mobile ready
• favicon
• Easy word press upload.
• design best practices
• -Home
• -About
• -Services
• - Contact Us
• - Privacy/Terms
• My site: plovenda.com
Nice to have
• Content ( can make ti better )
• Feed back on how to rank better.
Should not have
• Image here on website with no picture
• poor looking design,.

```html
<!DOCTYPE html>
<html lang="en">
<head>
<meta charset="utf-8">
<title>Plovenda — Brand Building &amp; Advertising</title>
<link href="https://fonts.googleapis.com/css2?family=Lora:wght@400;600;700&family=Open+Sans:wght@400;600;700&display=swap" rel="stylesheet">
<style>
:root{
  --orange:#f7931e;
  --navy:#1c3d6e;
  --ink:#2b2b2b;
  --text:#555a60;
  --muted:#8a8f96;
  --line:#e4e6ea;
  --paper:#ffffff;
  --soft:#f6f7f9;
  --footer:#2c2c2e;
  --footer-deep:#1f1f21;
}
*{box-sizing:border-box;margin:0;padding:0}
html,body{width:1200px;height:3548px;overflow:hidden;background:var(--paper)}
body{font-family:"Open Sans",Arial,sans-serif;color:var(--text);font-size:13px;line-height:1.6;position:relative}
.serif{font-family:"Lora",Georgia,serif}
a{color:inherit;text-decoration:none}
section,header,footer{position:relative;width:1200px}
.btn{display:inline-block;background:var(--orange);color:#fff;font-weight:600;font-size:13px;border-radius:20px;text-align:center}
.section-title{font-family:"Lora",Georgia,serif;font-weight:700;color:var(--ink);font-size:38px;text-align:center;line-height:1.2}

/* header */
.site-header{height:112px;display:flex;align-items:center;padding:0 88px 0 110px}
.brand{display:flex;align-items:center;gap:10px}
.brand-dot{width:14px;height:14px;border-radius:50%;background:var(--navy)}
.brand-name{font-family:"Lora",Georgia,serif;font-weight:700;font-size:32px;color:var(--orange)}
.main-nav{margin-left:auto;display:flex;align-items:center;gap:34px;font-size:14px;color:var(--ink)}
.main-nav .active{border:1px solid var(--navy);color:var(--navy);padding:4px 12px;font-weight:600}
.login{background:var(--navy);color:#fff;font-weight:600;padding:8px 36px;border-radius:4px;margin-left:40px}

/* hero */
.hero{height:588px;background:linear-gradient(100deg,#1a2c4a 0%,#3d5478 45%,#5b6c86 70%,#2d3c55 100%);text-align:center;color:#fff}
.hero-title{position:absolute;top:196px;left:0;right:0;font-family:"Lora",Georgia,serif;font-size:50px;line-height:1.25;font-weight:400}
.hero .btn{position:absolute;top:330px;left:540px;width:120px;padding:10px 0;border-radius:4px}
.dots{display:flex;justify-content:center;gap:8px}
.dots span{width:8px;height:8px;border-radius:50%;background:rgba(255,255,255,.6)}
.dots span.on{background:#fff}
.hero .dots{position:absolute;top:484px;left:0;right:0}

.mission{height:112px;background:var(--orange);color:#fff;font-weight:700;font-size:17px;line-height:1.5;display:flex;align-items:center;justify-content:center;text-align:center}

/* about */
.about{height:240px;text-align:center;padding-top:44px}
.about p{width:640px;margin:14px auto 0;font-size:12px;color:var(--text)}
.about .btn{margin-top:28px;padding:7px 28px}

/* services */
.services{height:852px;padding-top:12px;text-align:center}
.section-sub{width:380px;margin:8px auto 0;font-size:12px;color:var(--text)}
.service-card{position:absolute;width:320px;background:#fff;box-shadow:0 4px 18px rgba(0,0,0,.08);text-align:center;padding:44px 36px 0}
.service-card.featured{background:var(--navy);color:#d8e0ee}
.service-icon{width:74px;height:74px;border-radius:50%;background:var(--navy);margin:0 auto;display:flex;align-items:center;justify-content:center}
.featured .service-icon{background:var(--orange)}
.service-card h3{font-family:"Lora",Georgia,serif;font-weight:600;font-size:20px;color:var(--ink);margin-top:22px;line-height:1.25}
.featured h3{color:#fff}
.service-card p{font-size:12px;margin-top:10px}
.more-link{display:inline-block;margin-top:10px;font-size:12px;text-decoration:underline;color:var(--ink)}
.featured .more-link{color:#fff}

/* blogs */
.blogs{height:568px;text-align:center}
.blog-card{position:absolute;top:80px;width:320px;background:#fff;text-align:left;box-shadow:0 2px 10px rgba(0,0,0,.06)}
.blog-card.raised{box-shadow:0 8px 26px rgba(0,0,0,.14)}
.blog-photo{height:214px}
.blog-body{padding:14px 16px 18px}
.blog-meta{display:flex;gap:22px;font-size:11px;color:var(--muted)}
.blog-body h4{font-size:13px;font-weight:700;color:var(--ink);margin-top:12px}
.blog-body p{font-size:12px;margin-top:4px}
.blog-body .continue{display:inline-block;margin-top:10px;font-size:12px;color:var(--ink)}
.blogs .btn{position:absolute;top:484px;left:550px;padding:8px 0;width:100px}

/* testimonials */
.testimonials{height:464px;text-align:center}
.t-card{position:absolute;top:80px;width:320px;height:300px;background:#fff;box-shadow:0 4px 18px rgba(0,0,0,.09);padding:28px 34px 0;text-align:center}
.avatar{width:86px;height:86px;border-radius:50%;margin:0 auto;background:radial-gradient(circle at 50% 40%,#e7c9b0,#9a7057)}
.t-card h5{font-family:"Lora",Georgia,serif;font-weight:600;font-size:18px;color:var(--ink);margin-top:14px}
.t-role{font-size:11px;color:var(--muted)}
.t-card p{font-size:12px;margin-top:10px}
.stars{color:var(--orange);font-size:15px;letter-spacing:2px;margin-top:8px}
.quote{position:absolute;top:24px;font-family:"Lora",Georgia,serif;font-size:44px;line-height:1;color:var(--line)}
.arrow{position:absolute;top:200px;width:26px;height:26px;background:var(--navy);display:flex;align-items:center;justify-content:center}
.testimonials .dots{position:absolute;top:400px;left:0;right:0}
.testimonials .dots span{background:#f4c58c}
.testimonials .dots span.on{background:var(--orange)}

/* newsletter */
.newsletter{height:168px;border-top:1px solid var(--line);text-align:center;padding-top:30px}
.newsletter h2{font-size:30px}
.subscribe-row{display:flex;justify-content:center;gap:20px;margin-top:26px}
.subscribe-row .field{width:500px;height:38px;border:1px solid var(--line);border-radius:20px;text-align:left;padding:0 22px;line-height:36px;font-size:12px;color:var(--muted)}
.subscribe-row .btn{width:200px;height:38px;line-height:38px}

/* footer */
.site-footer{height:380px;background:var(--footer);color:#c9cacc}
.f-col{position:absolute;top:70px}
.f-col h6{font-family:"Lora",Georgia,serif;font-weight:600;font-size:18px;color:#fff;margin-bottom:12px}
.f-brand .brand-name{font-size:30px}
.f-brand p{width:200px;font-size:12px;margin-top:10px}
.f-brand .read{display:inline-block;margin-top:16px;font-size:12px;color:#fff}
.f-links li{list-style:none;font-size:12px;line-height:1.9;padding-left:14px;position:relative}
.f-links li::before{content:"";position:absolute;left:0;top:10px;width:4px;height:4px;background:var(--orange)}
.f-address .row{display:flex;gap:10px;font-size:12px;line-height:1.6;margin-bottom:6px}
.f-address svg{flex:none;margin-top:3px}
.f-form .line{display:flex;gap:6px}
.f-form .input{height:24px;background:#fff;color:var(--muted);font-size:10px;padding:4px 8px;border-radius:2px;flex:1}
.f-form .area{height:70px;background:#fff;color:var(--muted);font-size:10px;padding:6px 8px;margin-top:8px;border-radius:2px}
.f-form .btn{margin-top:12px;padding:5px 28px;font-size:12px}
.copy-bar{height:48px;background:var(--footer-deep);display:flex;align-items:center;padding:0 110px;color:#9a9b9e;font-size:11px}
.socials{margin-left:auto;display:flex;gap:10px}
.socials span{width:22px;height:22px;border-radius:50%;background:var(--orange)}
</style>
</head>
<body>

<header class="site-header">
  <a class="brand" href="#"><span class="brand-dot"></span><span class="brand-name">Plovenda</span></a>
  <nav class="main-nav">
    <a class="active" href="#">Home</a>
    <a href="#">About</a>
    <a href="#">Services</a>
    <a href="#">Blogs</a>
    <a href="#">Testimonials</a>
    <a href="#">Contact Us</a>
    <a class="login" href="#">Login</a>
  </nav>
</header>

<section class="hero" role="img" aria-label="Businessman in a suit working at a laptop in an office, dark blue toned">
  <h1 class="hero-title">Creating Strategies For<br>Measurable Results</h1>
  <a class="btn" href="#">Get In Touch</a>
  <div class="dots"><span></span><span class="on"></span><span></span><span></span></div>
</section>

<section class="mission">
  <p>We Help Small Business Owners Design And Execute Sustainable<br>Growth Strategies To Take Their Business To The Next Level</p>
</section>

<section class="about">
  <h2 class="section-title">About us</h2>
  <p>Founded in 2013, Plovenda is a professional small business marketing consulting firm. Focused on increasing company growth and profits, our team brings years of skill in branding and marketing.</p>
  <p>We have worked with several industry professionals and businesses across multiple cities, creating brand awareness and steady revenue growth.</p>
  <a class="btn" href="#">Read More</a>
</section>

<section class="services">
  <h2 class="section-title">Our Services</h2>
  <p class="section-sub">Lorem Ipsum is simply dummy text of the printing and typesetting industry. Lorem Ipsum has been the standard text.</p>

  <article class="service-card" style="left:100px;top:100px;height:320px">
    <div class="service-icon"><svg width="36" height="36" viewBox="0 0 36 36" fill="none" stroke="#fff" stroke-width="2.4"><circle cx="18" cy="18" r="14"/><circle cx="18" cy="18" r="8"/><circle cx="18" cy="18" r="2.5" fill="#fff"/></svg></div>
    <h3>Branding Design<br>and Strategy</h3>
    <p>Lorem Ipsum is simply dummy text of the printing and typesetting.</p>
    <a class="more-link" href="#">Read More</a>
  </article>

  <article class="service-card featured" style="left:440px;top:90px;height:340px">
    <div class="service-icon"><svg width="36" height="36" viewBox="0 0 36 36" fill="none" stroke="#fff" stroke-width="2.4"><path d="M18 5a9 9 0 0 0-5 16.5V25h10v-3.5A9 9 0 0 0 18 5z"/><path d="M14 29h8M15 32h6"/></svg></div>
    <h3>Marketing Plan Development<br>and Implementation</h3>
    <p>Lorem Ipsum is simply dummy text of the printing and typesetting.</p>
    <a class="more-link" href="#">Read More</a>
  </article>

  <article class="service-card" style="left:780px;top:100px;height:320px">
    <div class="service-icon"><svg width="36" height="36" viewBox="0 0 36 36" fill="none" stroke="#fff" stroke-width="2.4"><circle cx="14" cy="11" r="5"/><path d="M5 29c0-6 4-10 9-10s9 4 9 10"/><path d="M25 22l4-5 4 3"/></svg></div>
    <h3>Business<br>Consulting</h3>
    <p>Lorem Ipsum is simply dummy text of the printing and typesetting.</p>
    <a class="more-link" href="#">Read More</a>
  </article>

  <article class="service-card" style="left:270px;top:452px;height:310px">
    <div class="service-icon"><svg width="36" height="36" viewBox="0 0 36 36" fill="none" stroke="#fff" stroke-width="2.4"><path d="M8 6h16l4 4v20H8z"/><path d="M13 14h10M13 19h10M13 24h6"/></svg></div>
    <h3>Story Telling</h3>
    <p>Lorem Ipsum is simply dummy text of the printing and typesetting.</p>
    <a class="more-link" href="#">Read More</a>
  </article>

  <article class="service-card" style="left:610px;top:452px;height:310px">
    <div class="service-icon"><svg width="36" height="36" viewBox="0 0 36 36" fill="none" stroke="#fff" stroke-width="2.4"><path d="M6 15h6l14-7v20l-14-7H6z"/><path d="M11 21l2 8h4l-2-8"/></svg></div>
    <h3>Advertising</h3>
    <p>Lorem Ipsum is simply dummy text of the printing and typesetting.</p>
    <a class="more-link" href="#">Read More</a>
  </article>
</section>

<section class="blogs">
  <h2 class="section-title">Our Blogs</h2>

  <article class="blog-card" style="left:80px">
    <div class="blog-photo" role="img" aria-label="Couple sitting on the floor of a bright room with a laptop" style="background:linear-gradient(135deg,#e9e4dc,#c9bfb2 60%,#a79a8c)"></div>
    <div class="blog-body">
      <div class="blog-meta"><span>Mar 30, 2019</span><span>Jan 12</span><span>02</span></div>
      <h4>What is Lorem Ipsum?</h4>
      <p>Lorem Ipsum is simply dummy. The printing and typesetting industry. Lorem Ipsum has been the standard dummy.</p>
      <a class="continue" href="#">Continue →</a>
    </div>
  </article>

  <article class="blog-card raised" style="left:440px">
    <div class="blog-photo" role="img" aria-label="Modern kitchen interior with wooden cabinets" style="background:linear-gradient(135deg,#d8cfc2,#9c8470 55%,#5e4a3b)"></div>
    <div class="blog-body">
      <div class="blog-meta"><span>Mar 30, 2019</span><span>Jan 12</span><span>02</span></div>
      <h4>What is Lorem Ipsum?</h4>
      <p>Lorem Ipsum is simply dummy. The printing and typesetting industry. Lorem Ipsum has been the standard dummy.</p>
      <a class="continue" href="#">Continue →</a>
    </div>
  </article>

  <article class="blog-card" style="left:800px">
    <div class="blog-photo" role="img" aria-label="Open plan living room and kitchen with wood floors" style="background:linear-gradient(135deg,#cfd3d6,#8d7f70 55%,#6a5644)"></div>
    <div class="blog-body">
      <div class="blog-meta"><span>Mar 30, 2019</span><span>Jan 12</span><span>02</span></div>
      <h4>What is Lorem Ipsum?</h4>
      <p>Lorem Ipsum is simply dummy. The printing and typesetting industry. Lorem Ipsum has been the standard dummy.</p>
      <a class="continue" href="#">Continue →</a>
    </div>
  </article>

  <a class="btn" href="#">Read More</a>
</section>

<section class="testimonials">
  <h2 class="section-title">Testimonials</h2>
  <p class="section-sub" style="margin-top:4px">What clients say about us</p>

  <a class="arrow" style="left:108px" href="#"><svg width="10" height="10" viewBox="0 0 10 10" fill="none" stroke="#fff" stroke-width="2"><path d="M7 1L3 5l4 4"/></svg></a>
  <a class="arrow" style="left:1066px" href="#"><svg width="10" height="10" viewBox="0 0 10 10" fill="none" stroke="#fff" stroke-width="2"><path d="M3 1l4 4-4 4"/></svg></a>

  <article class="t-card" style="left:140px">
    <span class="quote" style="left:20px">“</span>
    <div class="avatar" role="img" aria-label="Client portrait"></div>
    <h5>Daniel Hart</h5>
    <div class="t-role">Creative Director</div>
    <p>Lorem Ipsum is simply dummy text of the printing and typesetting industry. Simply dummy text.</p>
    <div class="stars">★★★★★</div>
  </article>

  <article class="t-card" style="left:450px">
    <span class="quote" style="left:20px">“</span>
    <div class="avatar" role="img" aria-label="Client portrait"></div>
    <h5>Nadia Coles</h5>
    <div class="t-role">Creative Director</div>
    <p>Lorem Ipsum is simply dummy text of the printing and typesetting industry. Simply dummy text.</p>
    <div class="stars">★★★★★</div>
  </article>

  <article class="t-card" style="left:760px">
    <span class="quote" style="left:20px">“</span>
    <div class="avatar" role="img" aria-label="Client portrait"></div>
    <h5>Priya Lenard</h5>
    <div class="t-role">Creative Director</div>
    <p>Lorem Ipsum is simply dummy text of the printing and typesetting industry. Simply dummy text.</p>
    <div class="stars">★★★★★</div>
  </article>

  <div class="dots"><span class="on"></span><span></span><span></span></div>
</section>

<section class="newsletter">
  <h2 class="section-title">Join Our Newletter</h2>
  <div class="subscribe-row">
    <div class="field">Email Here</div>
    <a class="btn" href="#">Subscribe</a>
  </div>
</section>

<footer>
  <div class="site-footer">
    <div class="f-col f-brand" style="left:110px">
      <div class="brand"><span class="brand-dot" style="background:#fff"></span><span class="brand-name" style="color:#fff">Plovenda</span></div>
      <p>Lorem Ipsum is simply dummy text of the printing and typesetting field and is the industry.</p>
      <a class="read" href="#">Read More →</a>
    </div>

    <div class="f-col" style="left:372px">
      <h6>Quick Link</h6>
      <ul class="f-links">
        <li>Home</li><li>About us</li><li>Services</li><li>Testimonials</li><li>Blog</li><li>Contact us</li><li>Privacy/Terms</li>
      </ul>
    </div>

    <div class="f-col f-address" style="left:572px;width:220px">
      <h6>Company address</h6>
      <div class="row"><svg width="12" height="12" viewBox="0 0 12 12" fill="var(--orange)"><rect x="2" y="1" width="8" height="10" rx="1"/></svg><span>Plovenda, Inc.<br>1420 Harbor Lane Suite 210<br>Millbrook, OR 97001</span></div>
      <div class="row"><svg width="12" height="12" viewBox="0 0 12 12" fill="var(--orange)"><path d="M2 1h3l1 3-2 1a7 7 0 0 0 3 3l1-2 3 1v3a1 1 0 0 1-1 1A10 10 0 0 1 1 2a1 1 0 0 1 1-1z"/></svg><span>+1 (555) 014-2288</span></div>
      <div class="row"><svg width="12" height="12" viewBox="0 0 12 12" fill="var(--orange)"><path d="M2 1h3l1 3-2 1a7 7 0 0 0 3 3l1-2 3 1v3a1 1 0 0 1-1 1A10 10 0 0 1 1 2a1 1 0 0 1 1-1z"/></svg><span>+1 (555) 014-2290</span></div>
      <div class="row"><svg width="12" height="12" viewBox="0 0 12 12" fill="var(--orange)"><rect x="1" y="3" width="10" height="7"/></svg><span>+1 (555) 014-2291</span></div>
      <div class="row"><svg width="12" height="12" viewBox="0 0 12 12" fill="none" stroke="var(--orange)" stroke-width="1.5"><rect x="1" y="2.5" width="10" height="7"/><path d="M1 3l5 4 5-4"/></svg><span>info@plovenda.com</span></div>
    </div>

    <div class="f-col f-form" style="left:828px;width:262px">
      <h6>Contact us</h6>
      <div class="line"><div class="input">Name</div><div class="input">Email</div><div class="input">Phone</div></div>
      <div class="area">Message</div>
      <a class="btn" href="#">Subscribe</a>
    </div>
  </div>
  <div class="copy-bar">
    <span>Copyright @2019 Plovenda. All Right Reserve</span>
    <div class="socials"><span></span><span></span><span></span><span></span><span></span></div>
  </div>
</footer>

</body>
</html>
```